Hartwell Summit Electric van design

Looking to design a wrap for a 2021 halvorn trekline high roof using orange black and dark grey colors like in the logo

```html
<!DOCTYPE html>
<html lang="en">
<head>
<meta charset="utf-8">
<title>Hartwell Summit Electric – Van Wrap Side Panels</title>
<link rel="stylesheet" href="https://fonts.googleapis.com/css2?family=Montserrat:wght@600&family=Barlow:wght@500;600&family=Open+Sans:wght@700&display=swap">
<style>
  :root {
    --brand-orange: #e2613f;
    --brand-orange-ring: #e88466;
    --brand-black: #0b0b0b;
    --panel-white: #ffffff;
    --text-dark: #1d1d1d;
    --stage-top: #dadada;
    --stage-mid: #4a4a4a;
    --stage-deep: #222222;
    --stage-floor: #383838;
    --template-tint: rgba(225, 0, 0, 0.05);
  }
  html, body {
    margin: 0;
    padding: 0;
    width: 1200px;
    height: 954px;
    overflow: hidden;
  }
  body {
    background: linear-gradient(to bottom,
      var(--stage-top) 0%,
      #b3b3b3 12%,
      #7c7c7c 28%,
      var(--stage-mid) 45%,
      var(--stage-deep) 53.6%,
      var(--stage-floor) 53.7%,
      var(--stage-floor) 100%);
    position: relative;
  }
  .wrap-panel {
    position: absolute;
    left: 104.6px;
    width: 990.8px;
    height: 332.9px;
    display: block;
  }
  .wrap-panel--with-template { top: 100.2px; }
  .wrap-panel--clean { top: 567.2px; }
  .brand-name {
    font-family: "Montserrat", sans-serif;
    font-weight: 600;
    fill: var(--brand-black);
  }
  .service-item {
    font-family: "Barlow", sans-serif;
    font-weight: 500;
    font-size: 17px;
    letter-spacing: 0.6px;
    fill: var(--text-dark);
  }
  .service-arrow { fill: var(--brand-orange); }
  .partner-name {
    font-family: "Barlow", sans-serif;
    font-weight: 600;
    font-size: 29px;
    fill: var(--text-dark);
    letter-spacing: 0.5px;
  }
  .phone-number {
    font-family: "Open Sans", sans-serif;
    font-weight: 700;
    font-size: 54px;
    fill: var(--panel-white);
    letter-spacing: 1px;
  }
</style>
</head>
<body>

<svg class="wrap-panel wrap-panel--with-template" viewBox="0 0 1780 598" aria-label="Van side wrap with vehicle template">
  <defs>
    <g id="panel-artwork">
      <rect class="panel-base" x="0" y="0" width="1780" height="598" fill="var(--panel-white)"/>
      <polygon class="orange-field" points="0,0 295,0 660,598 0,598" fill="var(--brand-orange)"/>
      <polygon class="black-stripe" points="309,0 352,0 464,186 420,183" fill="var(--brand-black)"/>
      <polygon class="black-stripe" points="535,368 577,368 717,598 672,598" fill="var(--brand-black)"/>
      <polygon class="phone-band" points="690,523 1780,523 1780,598 737,598" fill="var(--brand-orange)"/>

      <g class="brand-lockup">
        <circle cx="545" cy="135" r="69" fill="var(--brand-orange)" stroke="var(--brand-orange-ring)" stroke-width="4"/>
        <text class="brand-name" x="646" y="126" font-size="56" letter-spacing="5">HARTWELL</text>
        <text class="brand-name" x="646" y="181" font-size="52" letter-spacing="0.5">Summit Electric</text>
      </g>

      <g class="service-list">
        <g transform="translate(528,243)"><path class="service-arrow" d="M0,2 H12 V-3 L22,5 L12,13 V8 H0 Z"/></g>
        <text class="service-item" x="563" y="253">Generator Installation</text>
        <g transform="translate(540,269)"><path class="service-arrow" d="M0,2 H12 V-3 L22,5 L12,13 V8 H0 Z"/></g>
        <text class="service-item" x="572" y="279">Service Upgrades</text>
        <g transform="translate(555,296)"><path class="service-arrow" d="M0,2 H12 V-3 L22,5 L12,13 V8 H0 Z"/></g>
        <text class="service-item" x="586" y="306">Low Voltage Wiring</text>
        <g transform="translate(570,322)"><path class="service-arrow" d="M0,2 H12 V-3 L22,5 L12,13 V8 H0 Z"/></g>
        <text class="service-item" x="601" y="332">3-Phase Service</text>
        <g transform="translate(588,346)"><path class="service-arrow" d="M0,2 H12 V-3 L22,5 L12,13 V8 H0 Z"/></g>
        <text class="service-item" x="619" y="356">Equipment Connections</text>
        <g transform="translate(603,375)"><path class="service-arrow" d="M0,2 H12 V-3 L22,5 L12,13 V8 H0 Z"/></g>
        <text class="service-item" x="634" y="385">Emergency Lighting</text>
        <g transform="translate(620,406)"><path class="service-arrow" d="M0,2 H12 V-3 L22,5 L12,13 V8 H0 Z"/></g>
        <text class="service-item" x="652" y="416">Code Violations</text>
        <g transform="translate(636,434)"><path class="service-arrow" d="M0,2 H12 V-3 L22,5 L12,13 V8 H0 Z"/></g>
        <text class="service-item" x="666" y="444">Warehouse Lighting</text>
      </g>

      <g class="partner-row">
        <text class="partner-name" x="890" y="424">VOLTMARA</text>
        <text class="partner-name" x="1058" y="428">KESTRION</text>
        <rect x="1220" y="394" width="36" height="36" rx="4" fill="var(--text-dark)"/>
        <text class="partner-name" x="1268" y="424">AMPWORTH</text>
      </g>

      <text class="phone-number" x="1007" y="580" text-anchor="middle">555.014.2290</text>
    </g>
  </defs>

  <use href="#panel-artwork"/>
  <rect class="vehicle-template" role="img" aria-label="Thin red outline of the high-roof van side, showing cab, windows, door and wheel arch placement over the artwork" x="70" y="5" width="1640" height="595" fill="var(--template-tint)"/>
</svg>

<svg class="wrap-panel wrap-panel--clean" viewBox="0 0 1780 598" aria-label="Van side wrap, artwork only">
  <use href="#panel-artwork"/>
</svg>

</body>
</html>
```